Labels for Bees Wax Candles & Honey Jars

We need labels for jars of natural honey. Most of our jars are square and the labels about 2" by 2".

Also we make bees wax candles of various sizes. We wish to wrap th enables around the circular candles which are between 2" and 3" in diameter... thus another have inch per label so they can be attached adhesively. The candles also vary in height... therefor th enables need to be 1.5", 2" and 3" in height.

We ar elooking for a very artistic and simple label that may include vibrant colors.
The name of our company must be displayed.. Candles by Morrow and for the Honey.... Morrow's All Natural Honey
Updates

The labels will be used for both Honey Jars as well as Bees Wax candles. There will be various sizes but that is something that can be adjusted after the initial design is approved. The Honey Jars should read "Natural Honey by Morrow" and the Candle labels should read "Natural Bees Wax Candles by Morrow" I am interested in simple, colorful, legible, and arty labels that pertain to bees and the natural environment. Hope this helps. We may also use a similar design on our web page. The size of the label on the honey will be 2" by 2" and the candles will vary.

Target Market(s)

Individual that purchase natural and organic products.

Requirements
Must have
• Labels should be very creative but legible and the emphasis on the candles should be all natural bees wax and the emphasis on the honey should be all natural honey. We are talking about the same design but different sizes and names.
Nice to have
• brillant colors and artistic

```html
<!DOCTYPE html>
<html lang="en">
<head>
<meta charset="utf-8">
<title>Natural Honey by Morrow — Jar Label</title>
<link rel="stylesheet" href="https://fonts.googleapis.com/css2?family=Josefin+Sans:wght@400;600&family=Sacramento&display=swap">
<style>
  :root {
    --page-bg: #f6f5f1;
    --label-border: #eef08c;
    --label-face: #ffffff;
    --honey: #f7b733;
    --art-tint-a: #fdf0cf;
    --art-tint-b: #fbe3a6;
  }
  * { box-sizing: border-box; margin: 0; padding: 0; }
  html, body {
    width: 799px;
    height: 1200px;
    overflow: hidden;
    background: var(--page-bg);
  }
  .canvas {
    position: relative;
    width: 799px;
    height: 1200px;
  }
  .label {
    position: absolute;
    left: 90px;
    top: 290px;
    width: 620px;
    height: 620px;
    background: var(--label-border);
    padding: 31px;
  }
  .label-face {
    position: relative;
    width: 100%;
    height: 100%;
    background: var(--label-face);
    overflow: hidden;
  }
  .art-placeholder {
    position: absolute;
    background: linear-gradient(160deg, var(--art-tint-a), var(--art-tint-b));
    border-radius: 4px;
  }
  .art-dipper {
    left: 146px;
    top: 8px;
    width: 159px;
    height: 179px;
  }
  .art-drops {
    left: 140px;
    top: 214px;
    width: 93px;
    height: 29px;
  }
  .divider {
    position: absolute;
    left: 31px;
    top: 264px;
    width: 494px;
    height: 2px;
    background: var(--honey);
  }
  .maker {
    position: absolute;
    left: 270px;
    top: 200px;
    font-family: "Sacramento", cursive;
    font-size: 60px;
    line-height: 1;
    color: var(--honey);
    white-space: nowrap;
  }
  .product-name {
    font-family: "Josefin Sans", sans-serif;
    color: var(--honey);
    line-height: 1;
  }
  .line-natural,
  .line-honey {
    position: absolute;
    left: 0;
    width: 100%;
    text-align: center;
    white-space: nowrap;
  }
  .line-natural {
    top: 300px;
    font-weight: 400;
    font-size: 100px;
    letter-spacing: -1px;
  }
  .line-honey {
    top: 392px;
    font-weight: 600;
    font-size: 122px;
    letter-spacing: 0;
  }
</style>
</head>
<body>
  <main class="canvas">
    <section class="label">
      <div class="label-face">
        <div class="art-placeholder art-dipper" role="img" aria-label="Illustration area: honey dipper with dripping honey"></div>
        <div class="art-placeholder art-drops" role="img" aria-label="Small decorative honey drops"></div>
        <p class="maker">by Morrow</p>
        <div class="divider"></div>
        <h1 class="product-name">
          <span class="line-natural">NATURAL</span>
          <span class="line-honey">HONEY</span>
        </h1>
      </div>
    </section>
  </main>
</body>
</html>
```